Upmarket cover for top management book, ideally unlike most common cover pages

This book is about both good management and mismanagement and introduces novel concepts such as the inverse exponential law in strategy, No doubt that these concepts will be criticized by some management scholars. However, students, a few other colleagues and key top managers find the new ideas useful and eye-opening.
The cover must help communicate a deeper vision of management as an expression of life creation and a sort of "divine" energy.

Practical details:
Print and ebook cover page plus elements of the cover for each of the three main book sections.
Title; The Harbor
Subtitle: Field methods and the quiet ripple rule
Author: Teodor M. Vasquel
Publisher: Brightwell Page Press
Width x height: 13,97 x 21,59 cm (without bleed)
Spine: 14-15 cm according to paper color

Target Market(s)

Mostly managers who did not have the opportunity of attending postgraduate management studies such as the MBA

Industry/Entity Type

Mostly high technology

Font styles to use
Serif
Sans Serif
Other font styles liked:
• Arial nova, Arial light

Requirements
Must have
• Preferably cover and back cover on white background, but any good proposals would do.
Nice to have
• An image of bright and reassuring, albeit potentially unlimited, strength. Ideally the cover design should show that good management is good for the COMMON GOOD of society
Should not have
• Please do not show images of people and no proposals reminiscent of other management and strategy book covers

```html
<!DOCTYPE html>
<html lang="en">
<head>
<meta charset="utf-8">
<title>The Harbor — Book Cover Spread</title>
<link rel="stylesheet" href="https://fonts.googleapis.com/css2?family=Barlow:wght@300;400;500;600;700&family=Playfair+Display:wght@700;900&display=swap">
<style>
  :root {
    --paper: #ffffff;
    --ink: #000000;
    --signal-red: #ff0000;
    --serif: "Playfair Display", serif;
    --sans: "Barlow", sans-serif;
  }
  html, body {
    margin: 0;
    padding: 0;
    width: 1200px;
    height: 885px;
    overflow: hidden;
    background: var(--paper);
  }
  .cover-spread {
    position: relative;
    width: 1200px;
    height: 885px;
    background: var(--paper);
    overflow: hidden;
    color: var(--ink);
  }
  .cover-art {
    position: absolute;
    inset: 0;
    width: 1200px;
    height: 885px;
  }
  .back-quote {
    position: absolute;
    left: 63px;
    top: 108px;
    width: 434px;
    margin: 0;
    font-family: var(--sans);
    font-weight: 400;
    font-size: 17.4px;
    line-height: 20.3px;
    text-align: right;
  }
  .quote-mark-bar {
    position: absolute;
    left: 509px;
    top: 113px;
    width: 8px;
    height: 49px;
    background: var(--ink);
  }
  .back-attribution {
    position: absolute;
    left: 63px;
    top: 537px;
    width: 460px;
    margin: 0;
    font-family: var(--sans);
    font-weight: 400;
    font-size: 15.5px;
    line-height: 20px;
  }
  .back-attribution strong {
    font-weight: 700;
    font-size: 17px;
  }
  .subtitle {
    position: absolute;
    left: 985px;
    top: 104px;
    margin: 0;
    font-family: var(--sans);
    font-weight: 600;
    font-size: 21px;
    line-height: 22px;
    color: var(--ink);
  }
  .author-front {
    position: absolute;
    left: 992px;
    top: 748px;
    margin: 0;
    font-family: var(--sans);
    font-weight: 500;
    font-size: 40px;
    line-height: 42px;
    letter-spacing: 0.5px;
    color: var(--ink);
  }
</style>
</head>
<body>
<main class="cover-spread">

  <svg class="cover-art" viewBox="0 0 1200 885" xmlns="http://www.w3.org/2000/svg" aria-hidden="true">
    <!-- front red field -->
    <path class="front-red-field" fill="var(--signal-red)"
          d="M965,0 H1200 V885 H986 C980,790 945,725 880,672 L965,600 Z"/>

    <!-- spine -->
    <g class="spine" fill="var(--ink)">
      <text class="spine-publisher" transform="translate(607,238) rotate(-90)"
            font-family="Barlow, sans-serif" font-weight="500" font-size="18">Brightwell Page Press</text>
      <text class="spine-author" transform="translate(613,602) rotate(-90)"
            font-family="Barlow, sans-serif" font-weight="500" font-size="29">TEODOR M. VASQUEL</text>
      <rect class="spine-divider" x="581" y="620" width="38" height="2"/>
      <text class="spine-title" transform="translate(611,851) rotate(-90)"
            font-family="Playfair Display, serif" font-weight="700" font-size="42">The Harbor</text>
    </g>

    <!-- front title -->
    <g class="front-title" fill="var(--ink)" font-family="Playfair Display, serif" font-weight="700">
      <text class="title-the" transform="translate(728,206) rotate(-90)" font-size="82">The</text>
      <text class="title-capital" x="742" y="209" font-size="300">H</text>
      <text class="title-row" x="900" y="337" font-size="260" letter-spacing="-8">ar</text>
      <rect class="title-hairline" x="1040" y="336" width="112" height="1"/>
      <text class="title-row" x="905" y="471" font-size="260" letter-spacing="-12">bo</text>
      <text class="title-row" x="830" y="672" font-size="260">r</text>
    </g>
  </svg>

  <span class="quote-mark-bar"></span>
  <p class="back-quote">“Professor Vasquel, an Italian, has produced a provocative treatise that is worthy of Orsino Valde and other great thinkers and places their discoveries in the real world of human organizations, to see whether science can contribute to making a manager’s job any easier in the competitive marketplace. To my knowledge, this is a pioneering idea. In brief, just as the chemist Piero Lanzi turned to literature, the chemist Teodor Vasquel uses the laws of the universe on the manager. I am reminded of the firm Ferrandi Pianoforte who changed the piano in the 20th century. Ferrandi applied the principles of acoustic engineering and physics to the business of constructing handcrafted pianos that produce beautiful music all over the world. The author goes one step further: he applies hard science to the soft art of management. The results, as you might expect, are eye-opening.”</p>

  <p class="back-attribution"><strong>Martin R. Ashworth</strong> Professor of Strategic Management, Northgate Campus University</p>

  <p class="subtitle">Field Methods<br>and the Quiet<br>Ripple Rule</p>

  <p class="author-front">TEODOR M.<br>VASQUEL</p>

</main>
</body>
</html>
```